Full cover (front, back and side of the book). 28 cm x 20 cm total (High 20 cm, width 13, side 2 cm) Front cover: Title of the author on top, centered (Mathieu Clavreux) Title: Counting the rivers Subtitle: Sailing keeper coastal Bottom and centered: attached logo (Vorelma Editions) in white, and edited eventualy. Side: From left to right: Editor logo (only "Vorelma" word, without the "Editions" word, title and author name Back cover: Left text column ) Bottom: space available for the bar coded price and 2 or 3 lines of text Right text column (approx 6.5 cm wide) Bottom of the right colum, center of the right column: same attached logo (Vorelma Editions) in white, and edited eventualy, with www.vorelma.example below the logo. Left Lateral margin of the back cover, this book should be almost 1 cm)
Colors
Designer to choose colors to be used in the design.

```html
<!DOCTYPE html>
<html lang="en">
<head>
<meta charset="utf-8">
<title>Counting the rivers — full cover</title>
<link rel="stylesheet" href="https://fonts.googleapis.com/css2?family=Cinzel:wght@400&family=Noto+Serif:wght@400;700&display=swap">
<style>
  :root {
    --slate: #4c5a67;
    --white: #ffffff;
    --mint: #eaf3e6;
    --ink: #26343d;
    --sky: #c9dcef;
    --island: #3f7a66;
    --lagoon-deep: #2f8fb8;
    --lagoon: #5fd0dc;
    --shallow: #c8f0ec;
  }
  * { margin: 0; padding: 0; box-sizing: border-box; }
  html, body { width: 1200px; height: 856px; overflow: hidden; background: var(--white); }
  .cover { position: relative; width: 1200px; height: 856px; }
  .back-and-spine {
    position: absolute; left: 0; top: 0; width: 641px; height: 856px; background: var(--slate);
  }
  .blurb {
    position: absolute; top: 116px; width: 190px;
    font-family: "Noto Serif", serif; font-size: 14px; line-height: 20px; color: var(--white);
  }
  .blurb--left { left: 74px; }
  .blurb--right { left: 322px; }
  .publisher-mark {
    position: absolute; font-family: "Noto Serif", serif; font-weight: 700; color: var(--white);
    text-align: center; line-height: 1.05;
  }
  .publisher-mark--back { left: 323px; top: 530px; width: 180px; font-size: 26px; }
  .price-box { position: absolute; left: 327px; top: 686px; width: 178px; height: 104px; background: var(--white); }
  .spine-text {
    position: absolute; left: 602px; transform-origin: 0 0; transform: rotate(90deg) translateY(-50%);
    color: var(--white); white-space: nowrap;
  }
  .spine-publisher { top: 32px; font-family: "Noto Serif", serif; font-weight: 700; font-size: 24px; letter-spacing: 1px; }
  .spine-title { top: 200px; font-family: "Cinzel", serif; font-size: 27px; letter-spacing: 1px; }
  .spine-author { top: 588px; font-family: "Noto Serif", serif; font-weight: 700; font-size: 20px; }
  .front {
    position: absolute; left: 641px; top: 0; width: 559px; height: 856px;
    background: linear-gradient(180deg, var(--sky) 0%, #d9e6f2 14%, var(--island) 18%, #4d8a72 27%, var(--lagoon-deep) 30%, #3fb2cf 42%, var(--lagoon) 55%, #8ee0e0 72%, var(--shallow) 100%);
  }
  .front-text { position: absolute; left: 0; width: 559px; text-align: center; }
  .author {
    top: 52px; font-family: "Noto Serif", serif; font-weight: 700; font-size: 42px; color: var(--mint);
    text-shadow: 1px 2px 3px rgba(0,0,0,0.35);
  }
  .title {
    top: 462px; font-family: "Cinzel", serif; font-size: 76px; line-height: 100px; color: var(--white);
    text-shadow: 1px 2px 4px rgba(0,0,0,0.3);
  }
  .subtitle { top: 668px; font-family: "Noto Serif", serif; font-size: 34px; color: var(--ink); }
  .publisher-mark--front { left: 0; width: 559px; top: 752px; font-size: 30px; text-shadow: 0 0 0 transparent; }
</style>
</head>
<body>
<div class="cover">
  <section class="back-and-spine">
    <p class="blurb blurb--left">Lorem ipsum dolor sit amet, consectetur adipiscing elit, sed eiusmod tempor incidunt ut labore et dolore magna aliqua. Ut enim ad minim veniam, quis nostrud exercitation ullamco laboris nisi ut aliquid ex ea commodi consequat. Quis aute iure reprehenderit in voluptate velit esse cillum dolore eu fugiat nulla pariatur. Excepteur sint obcaecat cupiditat non proident, sunt in culpa qui officia deserunt mollit anim id est laborum.</p>
    <p class="blurb blurb--right">Lorem ipsum dolor sit amet, consectetur adipiscing elit, sed eiusmod tempor incidunt ut labore et dolore magna aliqua. Ut enim ad minim veniam, quis nostrud exercitation ullamco laboris nisi ut aliquid ex ea commodi consequat. Quis aute iure reprehenderit in voluptate velit esse cillum dolore eu fugiat nulla pariatur. Excepteur sint obcaecat cupiditat non proident, sunt in culpa qui officia deserunt mollit anim id est laborum.</p>
    <div class="publisher-mark publisher-mark--back">Vorelma<br>Editions</div>
    <div class="price-box"></div>
    <div class="spine-text spine-publisher">VORELMA</div>
    <div class="spine-text spine-title">Counting the Rivers</div>
    <div class="spine-text spine-author">Mathieu Clavreux</div>
  </section>
  <section class="front" role="img" aria-label="Aerial photograph of a small propeller plane flying over a turquoise lagoon with green islands">
    <h2 class="front-text author">Mathieu Clavreux</h2>
    <h1 class="front-text title">Counting<br>the Rivers</h1>
    <p class="front-text subtitle">Sailing keeper coastal</p>
    <div class="publisher-mark publisher-mark--front">Vorelma<br>Editions</div>
  </section>
</div>
</body>
</html>
```